Quorvane Learning App for Children with Dyslexia

Project Description:

We are seeking a talented UI/UX designer to create engaging and intuitive designs for Quorvane, an innovative educational app designed to help children learn letters and words through a multisensory learning approach. The app aims to be particularly helpful for children with dyslexia, providing a supportive and interactive learning environment.

Key App Features & Design Requirements:

Account Creation Screen: Design a welcoming and straightforward sign-up page that allows users to register with their email or continue with Brindlewave. The design should be clean, focusing on user-friendliness and accessibility, adhering to our terms of service and privacy policy.

Main Screen Design: The main screen should allocate at least 4/6 of its height to the interactive drawing area. It needs to display word prompts in both correct and scrambled orders and include options to "Show all Words," "Play all words," and a search function. The interface should be vibrant, engaging, and easy to navigate for children.

Profile Section: Create a user-friendly profile page that allows users to edit their profile image, name, username, email, links, and bio. The design should be clean and encourage user engagement.

QuorTally Page: This section will display the user's learning progress, including rankings, a learning curve, and recently learned words. It should visually represent progress in a motivating and understandable way, suitable for a younger audience.

Visual and Auditory Feedback Implementation: Incorporate elements that support visual and auditory feedback, using dyslexia-friendly formats. This includes choosing appropriate colors, fonts, and auditory cues.

Accessibility and Customization Settings: Designs should include settings for adjusting visual contrast, font size, and the word list to accommodate individual preferences and needs.

Feel free to add more interactions and/or pages.

Design preferences:

Color Scheme: Use a bright, inviting color palette that stimulates learning and engagement without overwhelming the users.
Font Selection: Opt for fonts that are readable and accessible, particularly for users with dyslexia.
Icons and Graphics: Design custom icons and graphics that are cohesive with the app's theme and purpose. Illustrations should be simple, relatable, and supportive of the learning process.

Target Market(s)

Educational

Industry/Entity Type

Educational

Colors
0054AA
0677BA
7BADD7
CADEEF
E8F1F8
0094D4
00A9DD
6FCCEA
C7EBF8
E9F6FB

Requirements
Must have
• Educational app, a writing area, scoring and account management
Nice to have
• Statistics, Ranking Page, Settings and some nice visual features

```html
<!DOCTYPE html>
<html lang="en">
<head>
<meta charset="utf-8">
<title>Quorvane – App Screens</title>
<link href="https://fonts.googleapis.com/css2?family=Poppins:wght@400;500;600;700&display=swap" rel="stylesheet">
<style>
:root{
  --navy:#0054AA; --blue:#0677BA; --sky:#0094D4; --cyan:#00A9DD; --light:#6FCCEA;
  --mist:#E8F1F8; --ice:#E9F6FB; --bg:#ffffff; --panel:#f3f4f6; --ink:#1f2530;
  --muted:#6b7280; --line:#e3e6ea;
}
*{box-sizing:border-box;margin:0;padding:0}
html,body{width:1200px;height:646px;overflow:hidden;background:var(--bg);font-family:"Poppins",sans-serif;color:var(--ink)}
.canvas{position:relative;width:1200px;height:646px}
.screen-title{position:absolute;top:66px;width:216px;text-align:center;font-size:20px;font-weight:400;color:#2a2a2a}
.screen{position:absolute;top:109px;width:216px;height:468px;border-radius:26px;overflow:hidden;background:var(--panel)}
.abs{position:absolute}
.status-time{left:12px;top:16px;font-size:11px;color:#fff}
.status-icons{right:12px;top:19px}
.header-band{left:0;top:0;width:216px;background:linear-gradient(180deg,var(--cyan),var(--navy))}
.header-title{left:0;width:216px;text-align:center;color:#fff;font-weight:700;font-size:13.5px}
.card{background:#fff;border-radius:6px;box-shadow:0 1px 4px rgba(0,0,0,.08)}
.btn-primary{background:linear-gradient(180deg,var(--cyan),var(--sky));color:#fff;font-weight:600;font-size:7.5px;display:flex;align-items:center;justify-content:center;border-radius:4px}
.nav{left:0;width:216px;height:42px;background:#fff;display:flex;align-items:center;justify-content:space-around;padding:0 22px}
.nav-plus{width:18px;height:18px;border-radius:50%;background:var(--blue);display:flex;align-items:center;justify-content:center}

/* login */
.login{background:linear-gradient(180deg,#0aa6e0 0%,#0a8fd3 45%,var(--navy) 100%)}
.brand-name{left:0;top:86px;width:216px;text-align:center;font-size:32px;font-weight:700;color:#fff}
.brand-tag{left:0;top:140px;width:216px;text-align:center;font-size:9.5px;color:#fff}
.login-heading{left:0;top:210px;width:216px;text-align:center;font-size:12.5px;font-weight:600;color:#fff}
.login-sub{left:0;top:228px;width:216px;text-align:center;font-size:7.5px;color:#fff}
.field{left:18px;top:253px;width:180px;height:27px;background:#f1f1f1;border-radius:4px;font-size:7.5px;color:#666;padding-left:10px;display:flex;align-items:center}
.divider-text{left:22px;top:324px;width:172px;display:flex;align-items:center;gap:6px;color:#fff;font-size:7.5px}
.divider-text span{flex:1;height:1px;background:var(--light)}
.alt-login{left:18px;top:343px;width:180px;height:27px;background:#f1f1f1;border-radius:4px;display:flex;align-items:center;justify-content:center;gap:6px;font-size:8.5px;font-weight:500}
.alt-dot{width:10px;height:10px;border-radius:50%;background:var(--sky)}
.legal{left:0;top:406px;width:216px;text-align:center;font-size:7.5px;line-height:12px;color:#cfe3f5}
.legal b{color:#fff;font-weight:400}

/* main */
.points{right:8px;top:45px;font-size:7px;font-weight:600;color:#fff}
.drawing{left:15px;top:73px;width:191px;height:170px;display:flex;align-items:center;justify-content:center;font-size:11px;font-weight:500;color:#333}
.toggle{left:15px;top:254px;width:191px;height:29px;display:flex;border:1px solid var(--sky);border-radius:2px;overflow:hidden;font-size:8px}
.toggle div{flex:1;display:flex;align-items:center;justify-content:center}
.toggle .off{background:#fff;color:#555}
.toggle .on{background:var(--sky);color:#fff;font-weight:600}
.word{width:60px;height:34px;background:#fff;border-radius:3px;display:flex;align-items:center;justify-content:center;font-size:7px;font-weight:500;box-shadow:0 1px 2px rgba(0,0,0,.05)}

/* profile */
.avatar{border-radius:50%;background:radial-gradient(circle at 50% 40%,#d9c1b0,#8c6a55)}
.row-label{left:40px;font-size:6.5px;color:var(--muted)}
.row-value{left:40px;font-size:7.5px;font-weight:600;color:var(--ink)}
.row-divider{left:20px;width:175px;height:1px;background:var(--line)}
.chev{left:188px;font-size:9px;color:#333}
.row-icon{left:27px;width:7px;height:7px;border-radius:2px;background:#8a8f97}
.link-add{color:var(--sky)}

/* stats */
.tab{top:88px;height:23px;border-radius:12px;display:flex;align-items:center;justify-content:center;font-size:8px;background:#fff;color:#555}
.tab.active{background:var(--sky);color:#fff;font-weight:500}
.rank-card{top:120px;height:49px;border-radius:3px;color:#fff;padding:12px 0 0 7px}
.rank-card small{display:block;font-size:6.5px;font-weight:500}
.rank-card strong{display:block;font-size:14.5px;font-weight:700;line-height:18px;white-space:nowrap}
.chart-title{font-size:10.5px;font-weight:500}
.axis{font-size:6px;color:var(--muted)}
.word-item{left:19px;font-size:7.5px;color:#444}
</style>
</head>
<body>
<div class="canvas">

  <h2 class="screen-title" style="left:87px">Login</h2>
  <h2 class="screen-title" style="left:362px">Main Screen</h2>
  <h2 class="screen-title" style="left:632px">Profile</h2>
  <h2 class="screen-title" style="left:907px">QuorTally</h2>

  <!-- LOGIN -->
  <section class="screen login" style="left:87px">
    <div class="abs status-time">9:41</div>
    <svg class="abs status-icons" width="40" height="8" viewBox="0 0 40 8"><rect x="0" y="5" width="2" height="3" fill="#fff"/><rect x="3" y="3" width="2" height="5" fill="#fff"/><rect x="6" y="1" width="2" height="7" fill="#fff"/><path d="M14 3a6 6 0 0 1 8 0M16 5a3 3 0 0 1 4 0" stroke="#fff" stroke-width="1.2" fill="none"/><circle cx="18" cy="7" r="1" fill="#fff"/><rect x="27" y="1" width="12" height="6" rx="1.5" fill="#fff"/></svg>
    <div class="abs brand-name">Quorvane</div>
    <div class="abs brand-tag">Learn letters and words</div>
    <div class="abs login-heading">Create An Account</div>
    <div class="abs login-sub">Enter your email to sign up for this app</div>
    <div class="abs field">Email Address</div>
    <div class="abs btn-primary" style="left:18px;top:287px;width:180px;height:27px">SIGN UP WITH EMAIL</div>
    <div class="abs divider-text"><span></span>or continue with<span></span></div>
    <div class="abs alt-login"><i class="alt-dot"></i>Login with Brindlewave</div>
    <p class="abs legal">By clicking continue, you agree to our<br><b>Terms of Service</b> and <b>Privacy Policy</b></p>
  </section>

  <!-- MAIN -->
  <section class="screen" style="left:362px">
    <div class="abs header-band" style="height:115px"></div>
    <div class="abs status-time">9:41</div>
    <svg class="abs status-icons" width="40" height="8" viewBox="0 0 40 8"><rect x="0" y="5" width="2" height="3" fill="#fff"/><rect x="3" y="3" width="2" height="5" fill="#fff"/><rect x="6" y="1" width="2" height="7" fill="#fff"/><path d="M14 3a6 6 0 0 1 8 0M16 5a3 3 0 0 1 4 0" stroke="#fff" stroke-width="1.2" fill="none"/><circle cx="18" cy="7" r="1" fill="#fff"/><rect x="27" y="1" width="12" height="6" rx="1.5" fill="#fff"/></svg>
    <svg class="abs" style="left:8px;top:47px" width="11" height="8" viewBox="0 0 11 8"><path d="M0 1h11M0 4h11M0 7h11" stroke="#fff" stroke-width="1.3"/></svg>
    <div class="abs header-title" style="top:41px">Main Screen</div>
    <div class="abs points">16 Points</div>
    <div class="abs card drawing">Drawing Area</div>
    <div class="abs toggle"><div class="off">Show all Words</div><div class="on">Play all words</div></div>
    <div class="abs word" style="left:15px;top:292px">Word 1</div>
    <div class="abs word" style="left:80px;top:292px">Word 2</div>
    <div class="abs word" style="left:145px;top:292px">Word 3</div>
    <div class="abs word" style="left:15px;top:334px">Word 4</div>
    <div class="abs word" style="left:80px;top:334px">...</div>
    <div class="abs btn-primary" style="left:15px;top:380px;width:191px;height:30px;font-size:8px">SHOW ME THE RESULTS</div>
    <nav class="abs nav" style="top:427px">
      <svg width="7" height="7" viewBox="0 0 7 7"><circle cx="3" cy="3" r="2.2" stroke="#555" fill="none"/><path d="M4.6 4.6L6.6 6.6" stroke="#555"/></svg>
      <svg width="9" height="6" viewBox="0 0 9 6"><path d="M0 2L4.5 0L9 2L4.5 4Z M2 3v2.2h5V3" fill="#555"/></svg>
      <span class="nav-plus"><svg width="7" height="7" viewBox="0 0 7 7"><path d="M3.5 0v7M0 3.5h7" stroke="#fff" stroke-width="1.4"/></svg></span>
      <svg width="9" height="7" viewBox="0 0 9 7"><rect x="0" y="0" width="6" height="4" rx="1.5" fill="#555"/><rect x="3" y="2.5" width="6" height="4" rx="1.5" fill="#555"/></svg>
      <svg width="7" height="7" viewBox="0 0 7 7"><circle cx="3.5" cy="2" r="1.8" fill="#555"/><path d="M0 7a3.5 3 0 0 1 7 0Z" fill="#555"/></svg>
    </nav>
  </section>

  <!-- PROFILE -->
  <section class="screen" style="left:632px">
    <div class="abs header-band" style="height:116px"></div>
    <div class="abs status-time">9:41</div>
    <svg class="abs status-icons" width="40" height="8" viewBox="0 0 40 8"><rect x="0" y="5" width="2" height="3" fill="#fff"/><rect x="3" y="3" width="2" height="5" fill="#fff"/><rect x="6" y="1" width="2" height="7" fill="#fff"/><path d="M14 3a6 6 0 0 1 8 0M16 5a3 3 0 0 1 4 0" stroke="#fff" stroke-width="1.2" fill="none"/><circle cx="18" cy="7" r="1" fill="#fff"/><rect x="27" y="1" width="12" height="6" rx="1.5" fill="#fff"/></svg>
    <svg class="abs" style="left:6px;top:48px" width="6" height="9" viewBox="0 0 6 9"><path d="M5 1L1.5 4.5L5 8" stroke="#fff" stroke-width="1.3" fill="none"/></svg>
    <div class="abs header-title" style="top:42px">Profile</div>
    <div class="abs card" style="left:12px;top:88px;width:191px;height:311px"></div>
    <div class="abs avatar" role="img" aria-label="Profile photo of the user" style="left:80px;top:96px;width:54px;height:54px"></div>
    <div class="abs" style="left:124px;top:134px;width:18px;height:18px;border-radius:50%;background:var(--sky);display:flex;align-items:center;justify-content:center"><svg width="9" height="7" viewBox="0 0 9 7"><rect x="0" y="1.2" width="9" height="5.8" rx="1" fill="#fff"/><circle cx="4.5" cy="4" r="1.6" fill="var(--sky)"/></svg></div>
    <div class="abs" style="left:0;top:156px;width:216px;text-align:center;font-size:11px;font-weight:500">Edit profile image</div>

    <i class="abs row-icon" style="top:193px;border-radius:50%"></i>
    <div class="abs row-label" style="top:186px">Name</div>
    <div class="abs row-value" style="top:194px">Mara Quill</div>
    <div class="abs chev" style="top:193px">›</div>
    <div class="abs row-divider" style="top:210px"></div>

    <i class="abs row-icon" style="top:223px;border-radius:50%"></i>
    <div class="abs row-label" style="top:216px">Username</div>
    <div class="abs row-value" style="top:224px">@username</div>
    <div class="abs chev" style="top:223px">›</div>
    <div class="abs row-divider" style="top:244px"></div>

    <i class="abs row-icon" style="top:258px"></i>
    <div class="abs row-label" style="top:251px">Email</div>
    <div class="abs row-value" style="top:259px">mara@quorvane.test</div>
    <div class="abs chev" style="top:258px">›</div>
    <div class="abs row-divider" style="top:277px"></div>

    <svg class="abs" style="left:26px;top:285px" width="9" height="8" viewBox="0 0 9 8"><path d="M3.5 5L5.5 3M2.5 4L1.2 5.3a1.5 1.5 0 0 0 2 2L4.5 6M6.5 4L7.8 2.7a1.5 1.5 0 0 0-2-2L4.5 2" stroke="#8a8f97" fill="none"/></svg>
    <div class="abs row-label" style="top:283px">Links</div>
    <div class="abs row-value" style="top:295px">sitebox.test</div>
    <div class="abs row-value" style="top:308px">linkhub.test</div>
    <div class="abs row-value" style="top:320px">pagenest.test</div>
    <div class="abs row-value link-add" style="top:333px">+Add link</div>
    <div class="abs row-divider" style="top:348px"></div>

    <i class="abs row-icon" style="top:360px"></i>
    <div class="abs row-label" style="top:353px">Bio</div>
    <div class="abs row-value" style="top:361px;font-weight:500">A description of this user.</div>
    <div class="abs chev" style="top:360px">›</div>

    <nav class="abs nav" style="top:426px">
      <svg width="7" height="7" viewBox="0 0 7 7"><circle cx="3" cy="3" r="2.2" stroke="#555" fill="none"/><path d="M4.6 4.6L6.6 6.6" stroke="#555"/></svg>
      <svg width="9" height="6" viewBox="0 0 9 6"><path d="M0 2L4.5 0L9 2L4.5 4Z M2 3v2.2h5V3" fill="#555"/></svg>
      <span class="nav-plus"><svg width="7" height="7" viewBox="0 0 7 7"><path d="M3.5 0v7M0 3.5h7" stroke="#fff" stroke-width="1.4"/></svg></span>
      <svg width="9" height="7" viewBox="0 0 9 7"><rect x="0" y="0" width="6" height="4" rx="1.5" fill="#555"/><rect x="3" y="2.5" width="6" height="4" rx="1.5" fill="#555"/></svg>
      <svg width="7" height="7" viewBox="0 0 7 7"><circle cx="3.5" cy="2" r="1.8" fill="#555"/><path d="M0 7a3.5 3 0 0 1 7 0Z" fill="#555"/></svg>
    </nav>
  </section>

  <!-- QUORTALLY -->
  <section class="screen" style="left:907px">
    <div class="abs header-band" style="height:75px"></div>
    <div class="abs status-time">9:41</div>
    <svg class="abs status-icons" width="40" height="8" viewBox="0 0 40 8"><rect x="0" y="5" width="2" height="3" fill="#fff"/><rect x="3" y="3" width="2" height="5" fill="#fff"/><rect x="6" y="1" width="2" height="7" fill="#fff"/><path d="M14 3a6 6 0 0 1 8 0M16 5a3 3 0 0 1 4 0" stroke="#fff" stroke-width="1.2" fill="none"/><circle cx="18" cy="7" r="1" fill="#fff"/><rect x="27" y="1" width="12" height="6" rx="1.5" fill="#fff"/></svg>
    <svg class="abs" style="left:9px;top:47px" width="11" height="8" viewBox="0 0 11 8"><path d="M0 1h11M0 4h11M0 7h11" stroke="#fff" stroke-width="1.3"/></svg>
    <div class="abs header-title" style="top:40px">QuorTally</div>
    <div class="abs avatar" role="img" aria-label="Small profile photo of the user" style="left:191px;top:41px;width:18px;height:18px;border:1px solid #fff"></div>

    <div class="abs tab active" style="left:11px;width:57px">Ranking</div>
    <div class="abs tab" style="left:74px;width:77px">Correct Words</div>
    <div class="abs tab" style="left:158px;width:43px">Todo..</div>

    <div class="abs rank-card" style="left:12px;width:117px;background:linear-gradient(135deg,var(--cyan),var(--sky))"><small>Total Ranking</small><strong>1st Place of 100</strong></div>
    <div class="abs rank-card" style="left:133px;width:83px;background:linear-gradient(135deg,var(--blue),var(--navy))"><small>Daily Ranking</small><strong>10th Place</strong></div>

    <div class="abs card" style="left:12px;top:180px;width:191px;height:149px"></div>
    <div class="abs chart-title" style="left:19px;top:187px">Learning curve</div>
    <div class="abs axis" style="left:19px;top:212px">100 words per day</div>
    <div class="abs axis" style="left:19px;top:231px">50 words per day</div>
    <div class="abs axis" style="left:19px;top:249px">.......</div>
    <div class="abs axis" style="left:19px;top:268px">.......</div>
    <div class="abs axis" style="left:19px;top:288px">.......</div>
    <svg class="abs" style="left:0;top:0" width="216" height="468" viewBox="0 0 216 468">
      <g stroke="#e6e8eb" stroke-width=".6">
        <path d="M19 218H196M19 237H196M19 255H196M19 274H196M19 294H196M19 303H196"/>
      </g>
      <polyline points="20,306 50,303 77,287 85,290 120,268 128,270 144,251 154,262 165,242 175,248 186,219" fill="none" stroke="#1f6fe0" stroke-width="1.3" stroke-linejoin="round"/>
      <circle cx="186" cy="219" r="2.6" fill="#1f6fe0" stroke="#cfe1fb" stroke-width="1.5"/>
    </svg>
    <div class="abs axis" style="left:19px;top:310px;width:180px;display:flex;justify-content:space-between"><span>Nov</span><span>23</span><span>24</span><span>25</span><span>26</span><span>27</span><span>28</span><span>29</span><span>30</span></div>

    <div class="abs card" style="left:12px;top:339px;width:191px;height:99px"></div>
    <div class="abs chart-title" style="left:19px;top:346px">Recently learned words</div>
    <div class="abs word-item" style="top:364px">El</div>
    <div class="abs row-divider" style="left:19px;width:177px;top:378px"></div>
    <div class="abs word-item" style="top:380px">ELA</div>
    <div class="abs row-divider" style="left:19px;width:177px;top:394px"></div>
    <div class="abs word-item" style="top:396px">Lorem</div>
    <div class="abs row-divider" style="left:19px;width:177px;top:410px"></div>
    <div class="abs word-item" style="top:412px">Lorem</div>

    <nav class="abs nav" style="top:446px;height:22px;align-items:flex-start;padding-top:2px">
      <svg width="7" height="7" viewBox="0 0 7 7"><circle cx="3" cy="3" r="2.2" stroke="#555" fill="none"/><path d="M4.6 4.6L6.6 6.6" stroke="#555"/></svg>
      <svg width="9" height="6" viewBox="0 0 9 6"><path d="M0 2L4.5 0L9 2L4.5 4Z M2 3v2.2h5V3" fill="#555"/></svg>
      <span class="nav-plus" style="margin-top:-6px"><svg width="7" height="7" viewBox="0 0 7 7"><path d="M3.5 0v7M0 3.5h7" stroke="#fff" stroke-width="1.4"/></svg></span>
      <svg width="9" height="7" viewBox="0 0 9 7"><rect x="0" y="0" width="6" height="4" rx="1.5" fill="#555"/><rect x="3" y="2.5" width="6" height="4" rx="1.5" fill="#555"/></svg>
      <svg width="7" height="7" viewBox="0 0 7 7"><circle cx="3.5" cy="2" r="1.8" fill="#555"/><path d="M0 7a3.5 3 0 0 1 7 0Z" fill="#555"/></svg>
    </nav>
  </section>

</div>
</body>
</html>
```